Lumo Ket

Need business cards designed. Project is an Arts Center in Hollywood. It'll include 3 live theatre, a restaurant and event space.

Target Market(s)

Across the board, young and old.

Industry/Entity Type

Entertainment

Contact Information for Business Card

Be creative. This is a creative venture that I'm building.

```html
<!DOCTYPE html>
<html lang="en">
<head>
<meta charset="utf-8">
<title>Lumo Ket — Business Cards</title>
<link href="https://fonts.googleapis.com/css2?family=Cinzel:wght@400;600&family=Montserrat:wght@400&display=swap" rel="stylesheet">
<style>
  :root {
    --backdrop: #43463f;
    --card-edge: #1b1b1b;
    --card-black: #050505;
    --card-glow: #1e1e1e;
    --gold: #ecc650;
    --white: #f4f4f4;
    --rule: #6a6a6a;
  }
  * { margin: 0; padding: 0; box-sizing: border-box; }
  html, body { width: 1200px; height: 900px; overflow: hidden; }
  body { background: var(--backdrop); position: relative; font-family: "Montserrat", sans-serif; }

  .card {
    position: absolute;
    left: 174px;
    width: 456px;
    height: 280px;
    background: var(--card-edge);
    padding: 10px;
  }
  .card--front { top: 178px; }
  .card--back { top: 488px; }

  .card__face {
    position: relative;
    width: 100%;
    height: 100%;
    background: radial-gradient(ellipse at 55% 45%, var(--card-glow) 0%, var(--card-black) 55%);
    overflow: hidden;
  }

  .wordmark {
    font-family: "Cinzel", serif;
    font-weight: 600;
    color: var(--gold);
    white-space: nowrap;
    letter-spacing: 0.02em;
  }

  .card__logo {
    position: absolute;
    left: 16px;
    top: 114px;
    font-size: 21px;
  }

  .card__rule {
    position: absolute;
    left: 161px;
    top: 26px;
    width: 1px;
    height: 206px;
    background: linear-gradient(to bottom, transparent, var(--rule) 25%, var(--rule) 75%, transparent);
  }

  .contact {
    position: absolute;
    left: 176px;
    top: 65px;
    color: var(--white);
  }
  .contact__name {
    font-family: "Cinzel", serif;
    font-weight: 600;
    font-size: 16px;
    color: var(--gold);
    letter-spacing: 0.02em;
  }
  .contact__org {
    font-family: "Cinzel", serif;
    font-size: 11px;
    margin-top: 2px;
    letter-spacing: 0.03em;
  }
  .contact__list { list-style: none; margin-top: 12px; font-size: 12px; line-height: 18px; }
  .contact__list li { display: flex; align-items: flex-start; }
  .contact__icon { width: 12px; height: 12px; margin: 3px 10px 0 2px; flex: none; }
  .contact__list .indent { padding-left: 24px; }

  .card__pattern {
    position: absolute;
    left: 60px;
    top: 0;
    width: 316px;
    height: 260px;
    background: radial-gradient(ellipse at center, #232323 0%, #141414 45%, transparent 72%);
  }
  .card__back-logo {
    position: absolute;
    left: 0;
    right: 0;
    top: 104px;
    text-align: center;
    font-size: 26px;
  }
  .card__url {
    position: absolute;
    left: 0;
    right: 0;
    top: 170px;
    text-align: center;
    font-size: 11px;
    letter-spacing: 0.42em;
    color: #cfcfcf;
  }

  .hero-mark {
    position: absolute;
    left: 716px;
    top: 200px;
    width: 376px;
    text-align: center;
    font-size: 60px;
  }
</style>
</head>
<body>

  <section class="card card--front">
    <div class="card__face">
      <div class="card__logo wordmark">Lumo Ket</div>
      <div class="card__rule"></div>
      <div class="contact">
        <div class="contact__name">Dana Veyro</div>
        <div class="contact__org">Lumo Ket</div>
        <ul class="contact__list">
          <li>
            <svg class="contact__icon" viewBox="0 0 12 12"><path fill="#f4f4f4" d="M1 4c0-2 2-3 5-3s5 1 5 3l-2 1-1-1V3H4v1L3 5 1 4zM3 6h6l1 5H2z"/></svg>
            323.555.0147
          </li>
          <li>
            <svg class="contact__icon" viewBox="0 0 12 12"><rect x="0.5" y="2.5" width="11" height="7" fill="none" stroke="#f4f4f4"/><path d="M0.5 2.5 6 7l5.5-4.5" fill="none" stroke="#f4f4f4"/></svg>
            dveyro@lumoket.com
          </li>
          <li>
            <svg class="contact__icon" viewBox="0 0 12 12"><path d="M6 11.5S2 7 2 4.5a4 4 0 0 1 8 0C10 7 6 11.5 6 11.5z" fill="none" stroke="#f4f4f4" stroke-width="1.2"/><circle cx="6" cy="4.5" r="1.4" fill="#f4f4f4"/></svg>
            412 N. Marlow Ave.
          </li>
          <li class="indent">Los Angeles, CA 90012</li>
        </ul>
      </div>
    </div>
  </section>

  <section class="card card--back">
    <div class="card__face">
      <div class="card__pattern" role="img" aria-label="Dark damask ornament pattern behind the logo"></div>
      <div class="card__back-logo wordmark">Lumo Ket</div>
      <div class="card__url">www.lumoket.com</div>
    </div>
  </section>

  <div class="hero-mark wordmark">Lumo Ket</div>

</body>
</html>
```